Scheduled Servicing Forms

Corvella Systems requires two schedule servicing forms to be created on designer templates for our engineers to complete when servicing customers. We will complete these forms on a periodic basis, and send to the customer on completion of the work.
We have two forms that need to be created:
• Hybrid Cloud Customer Service
• Veltrix Cloud Customer Service
Please do not reference our website for ideas as its about to change. “Specialised Consulting” is our new go to market, not “Pushing the Boundaries of Technology. Our new website (still under development) is available at https://corvellasystems.qzt.net.au and will be officially launched shortly.
Our company theme is “Blue” and we want to keep a blue theme for the work.
Please ensure there is “Ample” space for engineers to write comments next to each audit item.
We have uploaded examples of the content that needs to be created for both form in Word and Excel format.
The designer must upload the source files (not just PDF) so we can edit the content on the forms at a later date.
The forms must be in standard A4 size (multiple pages).
Industry/Entity Type
Information Technology
Look and feel

```html
<!DOCTYPE html>
<html lang="en">
<head>
<meta charset="utf-8">
<title>Corvella Systems Scheduled Service Checklist</title>
<link rel="stylesheet" href="https://fonts.googleapis.com/css2?family=Open+Sans:ital,wght@0,400;0,600;0,700;1,700&display=swap">
<style>
  :root {
    --canvas: #ffffff;
    --page: #ffffff;
    --page-edge: #c9ccd1;
    --ink: #1d1f24;
    --muted: #5b5f66;
    --rule: #9aa0a8;
    --head-fill: #e9edf3;
    --blue-deep: #2f5fb3;
    --blue-mid: #7fa3dd;
    --blue-soft: #d7e3f6;
  }
  * { box-sizing: border-box; margin: 0; padding: 0; }
  html, body { width: 807px; height: 1200px; overflow: hidden; background: var(--canvas); }
  body { position: relative; font-family: "Open Sans", Arial, sans-serif; color: var(--ink); }

  .sheet {
    position: absolute; left: 135px; width: 540px;
    background: var(--page);
    border: 1px solid var(--page-edge);
    box-shadow: 0 1px 4px rgba(0,0,0,.18);
    overflow: hidden;
  }
  .sheet--first { top: 12px; height: 528px; }
  .sheet--second { top: 556px; height: 630px; }

  .corner-graphic {
    position: absolute; top: 0; right: 0; width: 300px; height: 110px;
    background: linear-gradient(200deg, var(--blue-soft) 0%, rgba(215,227,246,.5) 40%, rgba(255,255,255,0) 75%);
  }
  .edge-graphic {
    position: absolute; top: 0; right: 0; width: 60px; height: 100%;
    background: linear-gradient(90deg, rgba(255,255,255,0) 0%, var(--blue-soft) 35%, var(--blue-mid) 75%, var(--blue-deep) 100%);
    opacity: .85;
  }
  .edge-graphic--top {
    position: absolute; top: 0; left: 0; width: 100%; height: 22px;
    background: linear-gradient(180deg, var(--blue-soft), rgba(255,255,255,0));
  }

  .sheet-title {
    position: relative; text-align: center; margin-top: 14px;
    font-weight: 700; font-style: italic; font-size: 13px; line-height: 15px;
    color: var(--ink);
  }
  .sheet-fields { position: relative; margin: 12px 0 0 70px; font-size: 7px; color: var(--muted); }
  .sheet-fields div { display: flex; align-items: flex-end; height: 10px; }
  .sheet-fields span.line { display: inline-block; width: 90px; border-bottom: 1px solid var(--rule); margin-left: 4px; }

  .checklist {
    position: relative; border-collapse: collapse; width: 420px; margin-left: 60px;
    font-size: 6.4px; line-height: 8px;
  }
  .sheet--first .checklist { margin-top: 10px; }
  .sheet--second .checklist { margin-top: 34px; width: 400px; }
  .checklist th, .checklist td { border: 1px solid var(--rule); padding: 2px 5px; vertical-align: top; text-align: left; }
  .checklist th { background: var(--head-fill); font-weight: 700; font-size: 7px; height: 15px; vertical-align: middle; }
  .checklist td.task { width: 62%; }
  .checklist td.result { width: 38%; }
  .sheet--first .checklist td { height: 28px; }
  .sheet--second .checklist td { height: 29px; }

  .choice { display: flex; gap: 16px; }
  .choice span { display: inline-flex; align-items: center; gap: 3px; }
  .box { width: 6px; height: 6px; border: 1px solid var(--muted); display: inline-block; }
  .comment { display: flex; align-items: flex-end; margin-top: 2px; color: var(--muted); }
  .comment .line { flex: 1; border-bottom: 1px solid var(--rule); margin-left: 3px; height: 7px; }

  .recommendations { margin-top: 3px; color: var(--muted); }
  .recommendations li { list-style: none; display: flex; align-items: flex-end; height: 8px; }
  .recommendations li .line { flex: 1; border-bottom: 1px solid var(--rule); margin-left: 3px; }
</style>
</head>
<body>

<section class="sheet sheet--first">
  <div class="corner-graphic" role="img" aria-label="Faint blue angular graphic in the top corner"></div>
  <h1 class="sheet-title">Corvella Systems<br>Veltrix Hybrid/On-Premise<br>Scheduled Service Checklist</h1>
  <div class="sheet-fields">
    <div>Customer: <span class="line"></span></div>
    <div>Date: <span class="line"></span></div>
  </div>
  <table class="checklist">
    <thead><tr><th>Maintenance Check</th><th>Result</th></tr></thead>
    <tbody>
      <tr><td class="task">Active backups for all VMs and hosts checked: all jobs successful in the last 7 days</td><td class="result"><div class="choice"><span><i class="box"></i>Yes</span><span><i class="box"></i>No</span></div><div class="comment">Comment:<span class="line"></span></div></td></tr>
      <tr><td class="task">Test restore from backup copy</td><td class="result"><div class="choice"><span><i class="box"></i>Yes</span><span><i class="box"></i>No</span></div><div class="comment">Comment:<span class="line"></span></div></td></tr>
      <tr><td class="task">Test restore of an email</td><td class="result"><div class="choice"><span><i class="box"></i>Yes</span><span><i class="box"></i>No</span></div><div class="comment">Comment:<span class="line"></span></div></td></tr>
      <tr><td class="task">Test restore of a shared file</td><td class="result"><div class="choice"><span><i class="box"></i>Yes</span><span><i class="box"></i>No</span></div><div class="comment">Comment:<span class="line"></span></div></td></tr>
      <tr><td class="task">Inspect server hardware health and storage alerts; replace any failing drives</td><td class="result"><div class="choice"><span><i class="box"></i>Yes</span><span><i class="box"></i>No</span></div><div class="comment">Comment:<span class="line"></span></div></td></tr>
      <tr><td class="task">Check event logs</td><td class="result"><div class="choice"><span><i class="box"></i>Yes</span><span><i class="box"></i>No</span></div><div class="comment">Comment:<span class="line"></span></div></td></tr>
      <tr><td class="task">Check that all users have MFA enabled</td><td class="result"><div class="choice"><span><i class="box"></i>Yes</span><span><i class="box"></i>No</span></div><div class="comment">Comment:<span class="line"></span></div></td></tr>
      <tr><td class="task">Review mailbox rules and forwarding</td><td class="result"><div class="choice"><span><i class="box"></i>Yes</span><span><i class="box"></i>No</span></div><div class="comment">Comment:<span class="line"></span></div></td></tr>
      <tr><td class="task">Confirm directory sync is healthy</td><td class="result"><div class="choice"><span><i class="box"></i>Yes</span><span><i class="box"></i>No</span></div><div class="comment">Comment:<span class="line"></span></div></td></tr>
      <tr><td class="task">Review firewall and VPN policies</td><td class="result"><div class="choice"><span><i class="box"></i>Yes</span><span><i class="box"></i>No</span></div><div class="comment">Comment:<span class="line"></span></div></td></tr>
      <tr><td class="task">Review licence usage against active users</td><td class="result"><div class="choice"><span><i class="box"></i>Yes</span><span><i class="box"></i>No</span></div><div class="comment">Comment:<span class="line"></span></div></td></tr>
      <tr><td class="task">Check endpoint protection status</td><td class="result"><div class="choice"><span><i class="box"></i>Yes</span><span><i class="box"></i>No</span></div><div class="comment">Comment:<span class="line"></span></div></td></tr>
      <tr><td class="task">Check and record overall security score</td><td class="result">
        <div class="comment">Score:<span class="line"></span></div>
        <ol class="recommendations">
          <li>Top 5 Recommendations:</li>
          <li>1.<span class="line"></span></li>
          <li>2.<span class="line"></span></li>
          <li>3.<span class="line"></span></li>
          <li>4.<span class="line"></span></li>
          <li>5.<span class="line"></span></li>
        </ol>
      </td></tr>
    </tbody>
  </table>
</section>

<section class="sheet sheet--second">
  <div class="edge-graphic--top" role="img" aria-label="Soft blue band along the top edge"></div>
  <div class="edge-graphic" role="img" aria-label="Blue angular graphic down the right edge"></div>
  <table class="checklist">
    <tbody>
      <tr><td class="task">Confirm server disk space and rotate old log files</td><td class="result"><div class="choice"><span><i class="box"></i>Yes</span><span><i class="box"></i>No</span></div><div class="comment">Comment:<span class="line"></span></div></td></tr>
      <tr><td class="task">Review warranty status of all critical hardware</td><td class="result"><div class="choice"><span><i class="box"></i>Yes</span><span><i class="box"></i>No</span></div><div class="comment">Comment:<span class="line"></span></div></td></tr>
      <tr><td class="task">Review server uptime and restart if required</td><td class="result"><div class="choice"><span><i class="box"></i>Yes</span><span><i class="box"></i>No</span></div><div class="comment">Comment:<span class="line"></span></div></td></tr>
      <tr><td class="task">Review UPS battery health and run a self test</td><td class="result"><div class="choice"><span><i class="box"></i>Yes</span><span><i class="box"></i>No</span></div><div class="comment">Comment:<span class="line"></span></div></td></tr>
      <tr><td class="task">Review network switch and router firmware versions</td><td class="result"><div class="choice"><span><i class="box"></i>Yes</span><span><i class="box"></i>No</span></div><div class="comment">Comment:<span class="line"></span></div></td></tr>
      <tr><td class="task">Review wireless access points and guest network</td><td class="result"><div class="choice"><span><i class="box"></i>Yes</span><span><i class="box"></i>No</span></div><div class="comment">Comment:<span class="line"></span></div></td></tr>
      <tr><td class="task">Review printer queues and clear stalled jobs</td><td class="result"><div class="choice"><span><i class="box"></i>Yes</span><span><i class="box"></i>No</span></div><div class="comment">Comment:<span class="line"></span></div></td></tr>
      <tr><td class="task">Review scheduled tasks and confirm they ran as expected</td><td class="result"><div class="choice"><span><i class="box"></i>Yes</span><span><i class="box"></i>No</span></div><div class="comment">Comment:<span class="line"></span></div></td></tr>
      <tr><td class="task">Confirm all workstations have current patches applied</td><td class="result"><div class="choice"><span><i class="box"></i>Yes</span><span><i class="box"></i>No</span></div><div class="comment">Comment:<span class="line"></span></div></td></tr>
      <tr><td class="task">Review admin accounts and remove unused access</td><td class="result"><div class="choice"><span><i class="box"></i>Yes</span><span><i class="box"></i>No</span></div><div class="comment">Comment:<span class="line"></span></div></td></tr>
      <tr><td class="task">Confirm DNS and DHCP scopes are healthy</td><td class="result"><div class="choice"><span><i class="box"></i>Yes</span><span><i class="box"></i>No</span></div><div class="comment">Comment:<span class="line"></span></div></td></tr>
      <tr><td class="task">Update documentation and network diagram</td><td class="result"><div class="choice"><span><i class="box"></i>Yes</span><span><i class="box"></i>No</span></div><div class="comment">Comment:<span class="line"></span></div></td></tr>
      <tr><td class="task">Review remote access tools and remove unused agents</td><td class="result"><div class="choice"><span><i class="box"></i>Yes</span><span><i class="box"></i>No</span></div><div class="comment">Comment:<span class="line"></span></div></td></tr>
      <tr><td class="task">Check domain and certificate expiry dates</td><td class="result"><div class="choice"><span><i class="box"></i>Yes</span><span><i class="box"></i>No</span></div><div class="comment">Comment:<span class="line"></span></div></td></tr>
      <tr><td class="task">Review password policy and account lockout settings</td><td class="result"><div class="choice"><span><i class="box"></i>Yes</span><span><i class="box"></i>No</span></div><div class="comment">Comment:<span class="line"></span></div></td></tr>
      <tr><td class="task">Review storage replication and offsite copy status</td><td class="result"><div class="choice"><span><i class="box"></i>Yes</span><span><i class="box"></i>No</span></div><div class="comment">Comment:<span class="line"></span></div></td></tr>
      <tr><td class="task">Test failover of critical services where available</td><td class="result"><div class="choice"><span><i class="box"></i>Yes</span><span><i class="box"></i>No</span></div><div class="comment">Comment:<span class="line"></span></div></td></tr>
      <tr><td class="task">Review open service tickets with the customer</td><td class="result"><div class="choice"><span><i class="box"></i>Yes</span><span><i class="box"></i>No</span></div><div class="comment">Comment:<span class="line"></span></div></td></tr>
      <tr><td class="task">Check dark web monitoring report</td><td class="result"><div class="choice"><span><i class="box"></i>Yes</span><span><i class="box"></i>No</span></div><div class="comment">Comment:<span class="line"></span></div></td></tr>
    </tbody>
  </table>
</section>

</body>
</html>
```